Marrowind Integrated Health Brochures (2)

We need two brochures about whiplash treatment to be designed. One is for referring physicians, the other is for the patients they refer. I'd like a few design elements to tie the two together, but also have them be easily distinguishable from one another.
In our region we are considered the top soft tissue injury clinic. We are trying to increase the awareness of our referring physicians to the fact that we have an exceptional rate of success treating acceleration/deceleration injuries from motor vehicle accidents.
We understand the emotional toll of whiplash. We understand how pain robs people of their vitality and motivation. We help victims of whiplash reclaim their health and vitality.
We use Quillpress.com for our printing.
Logo, trifold brochure template, and text(pdf files) have been up;oaded to this project.
The text we have provided is what we want. There are two versions of it. One is for the brochure for patients, and one is for the brochure for doctors.

Target Market(s)

Physicians that will refer Whiplash victims to our clinic for soft tissue injury treatment.

Industry/Entity Type

Health

Font styles to use
Serif

Requirements
Must have
• professional graphics that compliment the text.
• All AI files, graphic files etc.
• Colors that work with the Logo.
• Fonts for company name can be found on our website: www.marrowindintegratedhealth.com
Nice to have
• We'd like it to have a nice visual flow. We have only provided the text we want. Titles can be different if the design choices would make sense with better titles. We want it to be convincing and calming, and project our sensitivity to those suffering and also prject our confidence in our long history of curing the condition.

```html
<!DOCTYPE html>
<html lang="en">
<head>
<meta charset="utf-8">
<title>Marrowind Integrated Health – Whiplash Brochure</title>
<link href="https://fonts.googleapis.com/css2?family=Crimson+Pro:wght@400;600&display=swap" rel="stylesheet">
<style>
:root{
  --lime-pale:#eef3ad;
  --lime:#c9df74;
  --forest:#1f5f2f;
  --sun:#f3ec6e;
  --sky:#1b6eb5;
  --teal:#1d8a96;
  --ember:#e05a24;
  --ink:#222;
  --paper:#fbfcef;
  --white:#fff;
}
*{margin:0;padding:0;box-sizing:border-box}
html,body{width:769px;height:1200px;overflow:hidden;background:var(--white)}
body{font-family:"Crimson Pro",Georgia,serif;color:var(--ink);position:relative}
.spread{position:absolute;left:0;width:769px;height:590px;overflow:hidden}
.spread--outside{top:0;background:var(--lime-pale)}
.spread--inside{top:610px;background:linear-gradient(180deg,#f3f8d6 0%,var(--paper) 30%,var(--paper) 75%,#eef5c9 100%)}
.spread svg.bg{position:absolute;left:0;top:0}
.fold{position:absolute;top:0;width:1px;height:590px;background:rgba(255,255,255,.35)}
.abs{position:absolute}
.headline{font-size:22px;font-weight:400;color:var(--sky);letter-spacing:.3px;white-space:nowrap}
.brand{display:flex;align-items:center;gap:6px;white-space:nowrap}
.brand__dot{width:24px;height:24px;border-radius:50%;background:var(--sky);flex:none}
.brand__name{font-weight:600;font-size:17px;color:var(--sky)}
.url{font-size:11.5px;color:var(--ink);letter-spacing:.3px}
.photo{position:absolute}
.thumb{position:absolute;border-radius:50%;border:2px solid var(--white)}
.symptoms-title{font-size:15px;line-height:16px;color:var(--sun);font-weight:400}
.symptoms{list-style:none;font-size:8.2px;color:var(--white);line-height:14.2px}
.symptoms li{padding-left:9px;position:relative}
.symptoms li::before{content:"";position:absolute;left:0;top:6px;width:3px;height:3px;background:var(--white)}
.on-green{font-size:7.8px;line-height:11.4px;color:var(--white)}
.promise{list-style:none;color:var(--sun);font-size:15.5px;line-height:18.5px}
.promise li{position:relative;padding-left:24px;margin-bottom:8px}
.promise li::before{content:"";position:absolute;left:0;top:4px;width:12px;height:12px;border-radius:50%;background:var(--white);box-shadow:0 0 0 2px #a8d2f3}
.copy{font-size:7.7px;line-height:11.4px;text-align:justify;color:var(--ink)}
.copy p{margin-bottom:10px}
.copy b{font-weight:600}
.emotion-title{font-size:14.5px;line-height:18px;color:var(--ember);font-weight:400}
.mission-lead{font-size:14px;color:var(--sky);line-height:18px}
.mission-life{font-size:15px;color:var(--sky);letter-spacing:2.5px}
.mission-sub{font-size:14px;color:var(--ember)}
.contact-icons{display:flex;flex-direction:column;gap:5px}
</style>
</head>
<body>

<section class="spread spread--outside">
  <svg class="bg" width="769" height="590" viewBox="0 0 769 590">
    <defs>
      <linearGradient id="greenFill" x1="0" y1="0" x2="0" y2="1">
        <stop offset="0" stop-color="#216634"/><stop offset="1" stop-color="#1c5a2c"/>
      </linearGradient>
    </defs>
    <path d="M0 108 C150 70 300 60 420 80 C560 100 660 110 769 92 L769 480 C680 500 600 520 500 525 C380 530 200 520 0 488 Z" fill="url(#greenFill)"/>
    <path d="M0 108 C150 70 300 60 420 80 C560 100 660 110 769 92" stroke="#dbe98a" stroke-width="3" fill="none"/>
  </svg>
  <div class="fold" style="left:253px"></div>
  <div class="fold" style="left:505px"></div>

  <h1 class="abs headline" style="left:52px;top:30px">The Treatment of Whiplash is Our Specialty</h1>

  <div class="abs brand" style="left:525px;top:34px">
    <span class="brand__dot"></span><span class="brand__name">Marrowind Integrated Health</span>
  </div>
  <div class="abs url" style="left:560px;top:64px;font-size:10.5px">www.marrowindintegratedhealth.com</div>

  <h2 class="abs symptoms-title" style="left:38px;top:114px">The most common symptoms<br>we see from whiplash:</h2>
  <ul class="abs symptoms" style="left:38px;top:152px;width:200px">
    <li>Headache</li><li>Neck Pain</li><li>Shoulder Pain</li><li>Upper Back Pain</li><li>Mid Back Pain</li><li>Low Back Pain</li>
    <li>Arm/Hand Numbness, and Pain</li><li>Jaw (TMJ) Pain and Dysfunction</li><li>Sciatica (Pain down legs)</li>
    <li>Slouching Posture</li><li>Rigid Posture</li><li>TBI (Traumatic Brain Injury)</li>
    <li>Brain Inflammation resulting in memory issues</li>
    <li>PTSD (flinching, anxiety, emotion-al upset) in<br>&nbsp;traffic, etc.</li>
  </ul>
  <p class="abs on-green" style="left:38px;top:368px;width:190px">These symptoms can last weeks, months or years. The long term consequences of untreated whiplash include premature spinal degeneration, as well as postural changes caused by muscle guarding (chronically tight muscles) which main-tains pain and limits function. Untreated whiplash can result in the establishment of a pernicious chronic pain cycle that can last a lifetime.</p>
  <div class="thumb" role="img" aria-label="Therapist treating a wrist" style="left:37px;top:488px;width:53px;height:53px;background:radial-gradient(#f1d7c4,#c9a58d)"></div>
  <div class="thumb" role="img" aria-label="Hands holding a shoulder" style="left:98px;top:500px;width:56px;height:56px;background:radial-gradient(#f0d8c8,#b9c6d6)"></div>
  <div class="thumb" role="img" aria-label="Massage of neck and shoulders" style="left:163px;top:502px;width:66px;height:66px;background:radial-gradient(#f2d6c3,#c29c86)"></div>

  <div class="photo" role="img" aria-label="Young woman holding her sore shoulder" style="left:253px;top:215px;width:252px;height:280px;background:radial-gradient(ellipse at 50% 45%,#f4e1d2 0%,#e8cdb7 35%,rgba(40,100,50,0) 70%)"></div>
  <div class="photo" role="img" aria-label="Cyclist riding under a cloudy sky" style="left:253px;top:478px;width:252px;height:60px;background:linear-gradient(180deg,#6e8fae,#b7c6d3 55%,#c9c2a8)"></div>
  <div class="abs url" style="left:253px;width:252px;top:552px;text-align:center">www.marrowindintegratedhealth.com</div>

  <ul class="abs promise" style="left:537px;top:150px;width:225px">
    <li>Massage for Whiplash</li>
    <li>Soft tissue injury treatment at Marrowind Integrated Health</li>
    <li>We know whiplash,<br>and how to treat it</li>
  </ul>
  <div class="photo" role="img" aria-label="Man's back with hands on a red painful neck area" style="left:515px;top:290px;width:240px;height:210px;background:radial-gradient(ellipse at 50% 40%,#e2574a 0%,#d9a995 25%,#bfb4ae 50%,rgba(31,95,47,0) 75%)"></div>
  <div class="thumb" role="img" aria-label="Therapist pressing on a shoulder" style="left:538px;top:500px;width:65px;height:65px;background:radial-gradient(#f1d9c6,#c9a48c)"></div>
  <div class="thumb" role="img" aria-label="Hands massaging a neck" style="left:613px;top:500px;width:57px;height:57px;background:radial-gradient(#f3dece,#d0ad95)"></div>
  <div class="thumb" role="img" aria-label="Hand massage" style="left:678px;top:490px;width:52px;height:52px;background:radial-gradient(#f2d3c2,#c78b7c)"></div>
</section>

<section class="spread spread--inside">
  <svg class="bg" width="769" height="590" viewBox="0 0 769 590">
    <path d="M0 0 H769 V58 C620 58 470 52 360 62 C240 75 110 92 0 95 Z" fill="var(--lime)"/>
    <path d="M0 540 C150 520 300 540 420 550 C560 560 660 530 769 520 V590 H0 Z" fill="var(--lime)"/>
    <rect x="262" y="30" width="500" height="32" fill="#f4f8dc" opacity=".8"/>
  </svg>
  <div class="fold" style="left:253px"></div>
  <div class="fold" style="left:525px"></div>

  <div class="abs brand" style="left:26px;top:36px">
    <span class="brand__dot" style="width:22px;height:22px"></span><span class="brand__name" style="font-size:16px">Marrowind Integrated Health</span>
  </div>
  <h2 class="abs headline" style="left:317px;top:34px">The Treatment of Whiplash is Our Specialty</h2>

  <h3 class="abs emotion-title" style="left:38px;top:112px">The Emotional Toll of<br>“The Invisible Injury”</h3>
  <div class="abs copy" style="left:38px;top:156px;width:188px">
    <p>Suffering from a whiplash injury can have far reaching affects. Many whiplash patients have reported to us that the condition causes a strain on the most important relationships in their lives. When spouses, children, friends and co-workers don't understand the whiplash victim's pain or their change in temperament, the social implications are clear. Since the in-jury is invisible (no casts or crutches), those in your life may not understand the significance of your injury, which can lead to frustration and stress in your relationships at home and at work.</p>
    <p>Patients who have whiplash report that it is often the little things they cannot do, like laun-dry, house chores, computer work, and dress-ing themselves, etc., that cause the most stress. Feelings of fragility, fear, anger, vul-nerability, guilt, shame, weakness, and victim-ization are common. It is also common for them to feel misunderstood, isolated, and alone in their suffering. This emotional stress can actually slow the recovery process.</p>
  </div>
  <div class="thumb" role="img" aria-label="Woman holding her aching jaw" style="left:22px;top:428px;width:82px;height:82px;border-color:#4aa8e0;background:radial-gradient(#f4dccb,#d7b7a0)"></div>
  <div class="thumb" role="img" aria-label="Blue target highlighting a painful joint" style="left:97px;top:462px;width:80px;height:80px;border-color:#4aa8e0;background:radial-gradient(#3fb0e6 0 18%,#f0d6c4 30%,#c7a891)"></div>
  <div class="thumb" role="img" aria-label="Woman stretching with a therapist" style="left:168px;top:458px;width:62px;height:62px;border-color:#4aa8e0;background:radial-gradient(#f1e3d6,#b7c3b0)"></div>

  <div class="photo" role="img" aria-label="Shirtless man holding his lower back" style="left:280px;top:90px;width:200px;height:310px;background:radial-gradient(ellipse at 50% 45%,#d8ad8f 0%,#c79b7c 30%,#3b3b3b 55%,rgba(251,252,239,0) 72%)"></div>
  <div class="abs copy" style="left:284px;top:392px;width:188px">
    <p>Most whiplash sufferers don't want to be seen as complainers, and so are often under diag-nosed with only neck pain and headaches, which are usually the most immediately recog-nizable symptoms.</p>
    <p>If you are suffering from a whiplash injury and are having similar experiences, do not despair. Our group of highly trained and experienced professionals at Marrowind Integrated Health have a proven record of successfully treating this condition. We specialize in the treatment of whiplash.</p>
  </div>
  <div class="abs url" style="left:253px;width:272px;top:552px;text-align:center;color:var(--teal);font-size:12.5px">www.marrowindintegratedhealth.com</div>

  <div class="photo" role="img" aria-label="Faint figure of a woman stretching" style="left:600px;top:230px;width:150px;height:280px;background:radial-gradient(ellipse at 60% 50%,rgba(150,150,150,.35),rgba(251,252,239,0) 70%)"></div>
  <div class="abs" style="left:542px;top:100px;width:215px">
    <div class="mission-lead">We are here to help you reclaim</div>
    <div class="mission-life">YOUR LIFE</div>
    <div class="mission-sub">Our Approach is in Our Mission</div>
  </div>
  <div class="abs copy" style="left:542px;top:162px;width:183px">
    <p><b>To Heal:</b> We work to alleviate the symptoms and the problems that cause the symptoms. From the short term goal of defeating the initial pain due to inflam-mation, to the long term goal of correcting the structural imbalance caused by muscle guarding, we strive to return our pa-tients to a pain free functional state.</p>
    <p><b>To Educate:</b> Patients gain a deeper under-standing of how the human body works through treatment, movement, stretching, and witness-ing the process of healing first hand. Many pa-tients consider the knowledge gained from treatment at our clinic as an unanticipated silver lining.</p>
    <p><b>To Empower:</b> Through the knowledge gained during the process of treatment at our facility, our patients are empowered, not only to avoid pain and dysfunc-tion, but more importantly to move towards ever greater health.</p>
    <p>We have earned and we work to keep the trust of referring Doctors, Physical Therapists, and other referring providers in the South Eastmere/North Calder County area.</p>
    <p>We have successfully treated thousands of whiplash cases and we look forward to putting our expertise to work for you.</p>
  </div>
  <div class="abs contact-icons" style="left:542px;top:520px">
    <svg width="12" height="12" viewBox="0 0 24 24"><path d="M6.6 10.8a15 15 0 006.6 6.6l2.2-2.2c.3-.3.7-.4 1-.2 1.1.4 2.3.6 3.6.6.6 0 1 .4 1 1V20c0 .6-.4 1-1 1A17 17 0 013 4c0-.6.4-1 1-1h3.5c.6 0 1 .4 1 1 0 1.3.2 2.5.6 3.6.1.3 0 .7-.2 1z" fill="#222"/></svg>
    <svg width="12" height="12" viewBox="0 0 24 24" fill="none" stroke="#222" stroke-width="2"><circle cx="12" cy="12" r="10"/><path d="M2 12h20M12 2a15 15 0 010 20M12 2a15 15 0 000 20"/></svg>
    <svg width="12" height="10" viewBox="0 0 24 18"><rect x="1" y="1" width="22" height="16" fill="none" stroke="#222" stroke-width="2"/><path d="M1 1l11 9 11-9" fill="none" stroke="#222" stroke-width="2"/></svg>
  </div>
</section>

</body>
</html>
```